Lukas turning 50 invitation

Celebrating my 50th years birthday party in the summer vacation village fjällbacka at the westcoast sweden. Se We have our summer house in that area. The party will be at main hotel where people will also stay. Theme of the evening is South American food, meat, caprinhia etc. not costume party though. Want a good looking and stylish invitation to send out a pdf. And possible printed. West coast Sweden is very much about blue sea and red and white houses I need to be able to update text myself.

Target Market(s)

My friends

Colors
33a6d7
0692cd
abd037
ffffff

Requirements
Must have
• Pictures of the small town Fjällbacka
Nice to have
• Just a Baltasar always and inviting feeling for a great party

```html
<!DOCTYPE html>
<html lang="en">
<head>
<meta charset="utf-8">
<title>Lukas Turning 50 – Invitation</title>
<link rel="stylesheet" href="https://fonts.googleapis.com/css2?family=Cormorant+Garamond:wght@500;600&family=Montserrat:wght@400;500&display=swap">
<style>
  :root {
    --page: #ffffff;
    --panel: #f3faf8;
    --frame: #1f8a55;
    --leaf-dark: #1f8f4e;
    --leaf-mid: #4cbf3f;
    --leaf-light: #abd037;
    --leaf-teal: #33a6d7;
    --title-green: #1e9a5a;
    --sky-blue: #1ea4e0;
    --muted: #8a8f93;
    --white: #ffffff;
  }
  * { box-sizing: border-box; margin: 0; padding: 0; }
  html, body { width: 848px; height: 1200px; overflow: hidden; background: var(--page); }
  .canvas { position: relative; width: 848px; height: 1200px; }

  .card {
    position: absolute; left: 42px; top: 28px; width: 750px; height: 1140px;
    box-shadow: 8px 10px 14px rgba(60, 50, 100, 0.35);
    overflow: hidden;
  }
  .foliage {
    position: absolute; inset: 0;
    background:
      radial-gradient(ellipse at 15% 20%, var(--leaf-mid) 0%, transparent 45%),
      radial-gradient(ellipse at 85% 25%, var(--leaf-teal) 0%, transparent 40%),
      radial-gradient(ellipse at 20% 80%, var(--leaf-light) 0%, transparent 45%),
      radial-gradient(ellipse at 80% 85%, var(--leaf-mid) 0%, transparent 45%),
      linear-gradient(160deg, var(--leaf-dark), var(--leaf-mid) 50%, var(--leaf-dark));
  }
  .panel {
    position: absolute; left: 108px; top: 92px; width: 550px; height: 535px;
    background: var(--panel);
  }
  .frame {
    position: absolute; left: 100px; top: 85px; width: 566px; height: 952px;
    border: 8px solid var(--frame);
  }
  .harbour-photo {
    position: absolute; left: 111px; top: 627px; width: 542px; height: 367px;
    background: linear-gradient(180deg, #7f9fc4 0%, #b9c3d3 38%, #9a8a7e 55%, #b4483d 64%, #5b7388 78%, #3e5468 100%);
  }
  .portrait {
    position: absolute; left: 298px; top: 36px; width: 173px; height: 232px;
    border: 7px solid var(--frame);
    background: linear-gradient(180deg, #3a4452 0%, #c9a48e 45%, #2a2f3a 100%);
  }

  .text { position: absolute; left: 108px; width: 550px; text-align: center; }
  .kicker {
    top: 310px; font-family: "Montserrat", sans-serif; font-weight: 400;
    font-size: 23px; letter-spacing: 0.24em; color: var(--title-green);
  }
  .details {
    top: 356px; font-family: "Montserrat", sans-serif; font-weight: 400;
    font-size: 23px; line-height: 36px; color: var(--sky-blue); text-transform: uppercase;
  }
  .headline {
    top: 485px; font-family: "Cormorant Garamond", serif; font-weight: 600;
    font-size: 74px; line-height: 1; color: var(--title-green);
  }
  .subline {
    top: 569px; font-family: "Montserrat", sans-serif; font-weight: 400;
    font-size: 21px; letter-spacing: 0.5em; color: var(--title-green);
  }
  .age {
    top: 590px; font-family: "Cormorant Garamond", serif; font-weight: 500;
    font-size: 230px; line-height: 1; color: var(--white);
    text-shadow: 2px 3px 6px rgba(0,0,0,0.25);
  }
  .rsvp {
    position: absolute; left: 0; top: 1174px; width: 848px; text-align: center;
    font-family: "Montserrat", sans-serif; font-size: 15px; letter-spacing: 0.35em;
    color: var(--muted);
  }
</style>
</head>
<body>
<div class="canvas">
  <div class="card">
    <div class="foliage" role="img" aria-label="Border of watercolour tropical leaves in greens and teal"></div>
    <div class="panel"></div>
    <div class="harbour-photo" role="img" aria-label="Photo of Fjällbacka harbour with boats and red and white houses"></div>
    <div class="frame"></div>
    <div class="portrait" role="img" aria-label="Portrait photo of Lukas"></div>

    <p class="text kicker">LET'S CELEBRATE!</p>
    <p class="text details">Saturday, November<br>10th at 7pm<br>Village Fjällbacka</p>
    <h1 class="text headline">Lukas Turning</h1>
    <p class="text subline">50TH BIRTHDAY</p>
    <p class="text age">50</p>
  </div>
  <p class="rsvp">RSVP TO LUKAS 12 48302175</p>
</div>
</body>
</html>
```